依頼詳細
購買意欲に響く電子チラシが欲しい。
記載項目
社名、情報、キャッチコピー
サイズ
A4
ページ数
片面
希望イメージ
シンプル 複雑
単色 カラフル
暗い 明るい
日常 高級
遊び心 厳粛
未来的 伝統的
女性的 男性的
希望する色
黄・オレンジ系、青系、無彩色系
納品ファイル
• 高解像度JPG (.jpg)
補足説明
販促用チラシの作成。

会員年齢層は平均40-50代が中心4000名ほど
見やすく、販促意欲を刺激するものを希望。

購入されたポイントは旅行やギフトを使えます。
会社ページ
https://www.lunafield-qz.app/

```html
<!DOCTYPE html>
<html lang="ja">
<head>
<meta charset="utf-8">
<title>一億円還元キャンペーン | Luna Field QZ</title>
<link rel="stylesheet" href="https://fonts.googleapis.com/css2?family=Noto+Sans+JP:wght@500;700;900&family=Roboto+Condensed:wght@700;800&display=swap">
<style>
:root{
  --navy:#14264a;
  --blue:#1f6fb8;
  --orange:#f28a14;
  --orange-deep:#e0661a;
  --yellow:#ffd23a;
  --red:#d8312b;
  --white:#ffffff;
}
*{margin:0;padding:0;box-sizing:border-box}
html,body{width:846px;height:1200px;overflow:hidden}
body{font-family:"Noto Sans JP",sans-serif;background:var(--white)}
.flyer{position:relative;width:846px;height:1200px;overflow:hidden}
.scene{position:absolute;inset:0;
  background:linear-gradient(180deg,#cfe9f7 0%,#9fd2ee 22%,#6ab7de 38%,#3e8fbd 48%,#c9b79a 62%,#b79a74 78%,#8c6f50 100%)}
.headline{position:absolute;left:24px;top:30px;color:var(--navy);font-weight:900;line-height:1;
  text-shadow:0 0 6px rgba(255,255,255,.9),0 0 14px rgba(255,255,255,.7)}
.headline .big{display:block;font-size:138px;letter-spacing:-2px}
.headline .sub{display:block;font-size:100px;letter-spacing:-3px;margin-top:8px}
.rate-tag{position:absolute;left:388px;top:60px;transform:rotate(-6deg);background:var(--orange);
  color:var(--white);font-weight:900;font-size:46px;padding:4px 18px;border-radius:10px;
  box-shadow:0 3px 0 var(--orange-deep)}
.lead{position:absolute;left:0;top:280px;width:846px;height:34px;background:linear-gradient(90deg,var(--blue),rgba(31,111,184,.6));
  color:var(--white);font-weight:700;font-size:24px;line-height:34px;padding-left:24px}
.lead em{font-style:normal;color:var(--yellow);font-weight:900}
.period{position:absolute;left:560px;top:334px;background:var(--navy);color:var(--white);font-weight:900;
  font-size:28px;padding:2px 22px;border-radius:4px}
.deadline{position:absolute;right:26px;top:372px;color:var(--navy);font-weight:900;font-size:40px;
  text-shadow:0 0 6px rgba(255,255,255,.9)}
.deadline .dow{display:inline-block;background:var(--navy);color:var(--white);border-radius:50%;width:42px;height:42px;
  font-size:26px;line-height:42px;text-align:center;vertical-align:middle;margin:0 2px;text-shadow:none}
.offers{position:absolute;left:0;top:440px;width:846px;list-style:none}
.offer{position:relative;height:104px;margin-bottom:20px}
.offer::before{content:"";position:absolute;left:0;top:40px;width:846px;height:64px;background:linear-gradient(90deg,rgba(20,38,74,.55),rgba(20,38,74,.25))}
.usual{position:absolute;left:14px;top:6px;font-size:22px;line-height:28px;font-weight:700;color:var(--white);text-shadow:0 1px 3px rgba(0,0,0,.6)}
.usual .chip{background:var(--red);color:var(--white);font-size:15px;padding:1px 6px;margin-right:6px;border-radius:3px;vertical-align:middle;text-shadow:none}
.usual .strike{text-decoration:line-through}
.base-rt{position:absolute;left:14px;top:43px;font-family:"Roboto Condensed",sans-serif;font-weight:800;font-size:58px;line-height:58px;color:var(--white);text-shadow:0 2px 4px rgba(0,0,0,.5)}
.arrow{position:absolute;left:268px;top:55px;width:0;height:0;border-left:26px solid var(--orange);border-top:17px solid transparent;border-bottom:17px solid transparent}
.saving{position:absolute;left:322px;top:0;z-index:2;background:var(--white);border-radius:6px;padding:0 12px;height:36px;
  font-weight:900;font-size:28px;line-height:36px;color:var(--orange)}
.saving small{font-size:17px;color:var(--red);margin-left:2px}
.bonus-rt{position:absolute;left:320px;top:43px;font-family:"Roboto Condensed",sans-serif;font-weight:800;font-size:64px;line-height:58px;color:var(--white);text-shadow:0 2px 4px rgba(0,0,0,.5)}
.bonus-rt .unit{font-size:56px}
.badge{position:absolute;right:24px;top:20px;width:78px;height:78px;border-radius:50%;background:var(--orange);border:3px solid var(--white);
  color:var(--white);text-align:center;font-weight:900;line-height:1.05;padding-top:12px;font-size:13px}
.badge b{display:block;font-family:"Roboto Condensed",sans-serif;font-size:28px}
.badge span{font-size:14px}
.footer{position:absolute;left:0;bottom:0;width:846px;height:120px;background:linear-gradient(180deg,rgba(255,255,255,0),rgba(255,255,255,.75) 40%);text-align:center}
.note{padding-top:42px;color:var(--navy);font-weight:700;font-size:20px}
.brand{margin-top:10px;color:var(--navy);font-weight:900;font-size:24px;letter-spacing:1px}
</style>
</head>
<body>
<main class="flyer">
  <div class="scene" role="img" aria-label="南国のビーチ、ヤシの木と青空、砂浜に置かれたデッキチェアの写真"></div>

  <h1 class="headline"><span class="big">一億円</span><span class="sub">還元キャンペーン</span></h1>
  <div class="rate-tag">RT付与率UP</div>

  <p class="lead">確定した報酬からRTに変換すると通常より<em>断然お得！</em></p>
  <p class="period">期間限定</p>
  <p class="deadline">2023年5月31日<span class="dow">水</span>まで</p>

  <ul class="offers">
    <li class="offer">
      <p class="usual"><span class="chip">通常</span><span class="strike">500,000円分</span></p>
      <p class="base-rt">350RT</p><span class="arrow"></span>
      <p class="saving">125,000<small>円 お得!</small></p>
      <p class="bonus-rt">437.5<span class="unit">RT</span></p>
      <p class="badge">付与率<b>25</b><span>%UP</span></p>
    </li>
    <li class="offer">
      <p class="usual"><span class="chip">通常</span><span class="strike">200,000円分</span></p>
      <p class="base-rt">140RT</p><span class="arrow"></span>
      <p class="saving">40,000<small>円 お得!</small></p>
      <p class="bonus-rt">168<span class="unit">RT</span></p>
      <p class="badge">付与率<b>20</b><span>%UP</span></p>
    </li>
    <li class="offer">
      <p class="usual"><span class="chip">通常</span><span class="strike">100,000円分</span></p>
      <p class="base-rt">70RT</p><span class="arrow"></span>
      <p class="saving">15,000<small>円 お得!</small></p>
      <p class="bonus-rt">80.5<span class="unit">RT</span></p>
      <p class="badge">付与率<b>15</b><span>%UP</span></p>
    </li>
    <li class="offer">
      <p class="usual"><span class="chip">通常</span><span class="strike">50,000円分</span></p>
      <p class="base-rt">35RT</p><span class="arrow"></span>
      <p class="saving">5,000<small>円 お得!</small></p>
      <p class="bonus-rt">38.5<span class="unit">RT</span></p>
      <p class="badge">付与率<b>10</b><span>%UP</span></p>
    </li>
    <li class="offer">
      <p class="usual"><span class="chip">通常</span><span class="strike">25,000円分</span></p>
      <p class="base-rt">17.5RT</p><span class="arrow"></span>
      <p class="saving">1,250<small>円 お得!</small></p>
      <p class="bonus-rt">18.5<span class="unit">RT</span></p>
      <p class="badge">付与率<b>5</b><span>%UP</span></p>
    </li>
  </ul>

  <footer class="footer">
    <p class="note">購入されたポイントは旅行やギフトに使えます</p>
    <p class="brand">Luna Field QZ</p>
  </footer>
</main>
</body>
</html>
```